Selling my Home Flyer

I need a flyer/brochure for a house listing I am putting together. I will put all of the information together for you to include in the flyer. This will only be a front and back flyer. No extra pages and no staples will be seen. This will be printed by a large office copier, not a professional copier on standard paper. Therefore no crazy dark backgrounds with lots of bleeding colors. Pictures that I want need for sure in there are Aerial with outline, Front from left, and one of the ones showing the large yard. I included a couple sample designs that I don't hate. But feel free to get creative. I will need this on a quick turnaround and I will make comments quickly as well, so submit ASAP.

Target Market(s)

People that will by my house.

Industry/Entity Type

Real Estate Agent

Font styles to use
Serif
Sans Serif

Colors

Designer to choose colors to be used in the design.

Requirements
Must have
• The pictures I mentioned above. And the price and SF and address! I forgot to tell you the address. It is 4817 Birchwell Lane, Palm Beach Gardens, FL 33410.
Should not have
• Anarchy. I don't want it to look too crazy. Should be pretty straight forward.

```html
<!DOCTYPE html>
<html lang="en">
<head>
<meta charset="utf-8">
<title>Birchwell Court Center – Listing Flyer</title>
<link rel="stylesheet" href="https://fonts.googleapis.com/css2?family=Cinzel:wght@500;600&family=Poppins:wght@400;500;600;700;800&display=swap">
<style>
  :root {
    --blue: #1a6a9e;
    --yellow: #fdd10b;
    --red: #e0193a;
    --ink: #1b1b1b;
    --white: #ffffff;
    --backdrop: #d9d9d9;
    --serif: "Cinzel", Georgia, serif;
    --sans: "Poppins", Arial, sans-serif;
  }
  * { box-sizing: border-box; margin: 0; padding: 0; }
  html, body { width: 1200px; height: 1142px; overflow: hidden; background: var(--backdrop); font-family: var(--sans); color: var(--ink); }
  .spread { position: relative; width: 1200px; height: 1142px; display: flex; gap: 20px; padding: 161px 20px; }
  .page { width: 570px; height: 820px; background: var(--white); display: flex; flex-direction: column; overflow: hidden; box-shadow: 0 6px 18px rgba(0,0,0,.25); }

  .photo { display: block; width: 100%; height: 100%; }
  .photo--exterior { background: linear-gradient(180deg, #8fc3ea 0%, #d9d2c4 45%, #5f8f3c 80%, #3e6a2a 100%); }
  .photo--dusk { background: linear-gradient(180deg, #5a6f8a 0%, #e6a66a 30%, #d9d5cc 55%, #4d6b33 85%, #2f4a22 100%); }
  .photo--interior { background: linear-gradient(180deg, #f2efe8 0%, #d9d2c6 60%, #9a8a77 100%); }
  .photo--kitchen { background: linear-gradient(180deg, #f4f4f2 0%, #cfd0cc 55%, #8d8a84 100%); }
  .photo--pool { background: linear-gradient(180deg, #6d7a86 0%, #b9c1c6 40%, #19a3c2 70%, #0f7a96 100%); }
  .photo--yard { background: linear-gradient(180deg, #7a8ba0 0%, #d8b890 35%, #c9c3b5 55%, #4f8a32 100%); }
  .photo--walkway { background: linear-gradient(180deg, #9ccbec 0%, #e6e1d6 50%, #a5866a 80%, #5c8a3a 100%); }
  .photo--laundry { background: linear-gradient(180deg, #eceae5 0%, #c8c5be 60%, #8b857b 100%); }
  .photo--bath { background: linear-gradient(180deg, #b78462 0%, #d9c1a7 50%, #f1ece4 100%); }

  /* Front */
  .front-header { background: var(--blue); height: 150px; flex: none; padding: 22px 26px 0; color: var(--white); }
  .front-title { font-family: var(--serif); font-weight: 600; font-size: 31px; letter-spacing: .5px; line-height: 1; white-space: nowrap; }
  .address-strip { display: inline-block; background: var(--yellow); color: var(--ink); font-weight: 700; font-size: 14px; padding: 4px 16px; margin-top: 12px; text-transform: uppercase; white-space: nowrap; }
  .front-subtitle { font-weight: 700; font-size: 17px; margin-top: 10px; padding-left: 16px; text-transform: uppercase; letter-spacing: .3px; white-space: nowrap; }

  .hero { position: relative; height: 226px; flex: none; margin: 8px 10px 0; }
  .price-card { position: absolute; right: 0; top: 84px; width: 196px; background: rgba(255,255,255,.92); padding-bottom: 10px; }
  .price-tag { background: var(--yellow); font-weight: 700; font-size: 17px; padding: 4px 14px; clip-path: polygon(12px 0, 100% 0, 100% 100%, 12px 100%, 0 50%); }
  .price { color: var(--red); font-weight: 800; font-size: 30px; padding: 2px 14px 4px; line-height: 1.1; }
  .facts { list-style: none; padding: 0 12px; }
  .facts li { display: flex; gap: 6px; font-size: 13px; font-weight: 500; line-height: 1.3; margin-top: 4px; }
  .facts svg { flex: none; margin-top: 3px; }

  .thumbs { display: grid; grid-template-columns: repeat(3, 1fr); gap: 6px; height: 150px; flex: none; margin: 6px 10px 0; }
  .feature { height: 200px; flex: none; margin: 6px 10px 0; }

  .footer { margin-top: auto; flex: none; display: flex; align-items: center; gap: 10px; height: 72px; border-top: 1px solid #eee; }
  .brand { background: var(--yellow); width: 120px; flex: none; height: 100%; display: flex; align-items: center; justify-content: center; }
  .brand-name { font-family: var(--serif); font-weight: 600; font-size: 15px; color: var(--ink); text-align: center; line-height: 1.05; }
  .contact { flex: 1; min-width: 0; padding-left: 4px; white-space: nowrap; }
  .contact-lead { font-size: 10.5px; }
  .contact-name { font-weight: 800; font-size: 19px; color: var(--blue); line-height: 1.15; }
  .reach { flex: none; padding-right: 14px; white-space: nowrap; }
  .phone { display: flex; align-items: center; gap: 4px; font-weight: 800; font-size: 20px; line-height: 1; }
  .email { display: flex; align-items: center; gap: 5px; font-size: 10.5px; font-weight: 600; margin-top: 5px; }

  /* Back */
  .back-header { background: var(--yellow); height: 100px; flex: none; display: flex; align-items: center; justify-content: center; text-align: center; }
  .back-title { font-family: var(--serif); font-weight: 600; font-size: 23px; line-height: 1.2; letter-spacing: .5px; white-space: nowrap; }
  .back-hero { height: 200px; flex: none; margin: 6px 10px 0; }
  .back-thumbs { display: grid; grid-template-columns: repeat(3, 1fr); gap: 6px; height: 130px; flex: none; margin: 6px 10px 0; }
  .details { background: var(--blue); color: var(--white); margin: 8px 10px 0; padding: 12px 14px; display: grid; grid-template-columns: 1fr 1fr; gap: 16px; flex: none; font-size: 10px; line-height: 1.35; font-weight: 500; }
  .details p + p { margin-top: 7px; }
  .details ul { list-style: none; }
  .details li { position: relative; padding-left: 13px; }
  .details li + li { margin-top: 6px; }
  .details li::before { content: ""; position: absolute; left: 0; top: 3px; width: 7px; height: 7px; border-radius: 50%; background: var(--yellow); }
  .back-lower { display: grid; grid-template-columns: repeat(3, 1fr); gap: 6px; flex: 1; min-height: 70px; margin: 6px 10px 6px; }
</style>
</head>
<body>
<main class="spread">

  <section class="page page--front">
    <header class="front-header">
      <h1 class="front-title">BIRCHWELL COURT CENTER</h1>
      <div class="address-strip">4817 Birchwell Lane, Palm Beach Gardens, FL 33410.</div>
      <p class="front-subtitle">Pool faced apartment available for lease</p>
    </header>

    <div class="hero">
      <div class="photo photo--exterior" role="img" aria-label="Front view of the two-storey stucco home from the left, with palms and landscaped garden"></div>
      <div class="price-card">
        <div class="price-tag">Offered at :</div>
        <div class="price">$570,000</div>
        <ul class="facts">
          <li><svg width="10" height="10" viewBox="0 0 10 10"><circle cx="5" cy="5" r="5" fill="#e0193a"/><path d="M4 2.8 6.2 5 4 7.2" stroke="#fff" stroke-width="1.4" fill="none"/></svg>2,307 SF</li>
          <li><svg width="10" height="10" viewBox="0 0 10 10"><circle cx="5" cy="5" r="5" fill="#e0193a"/><path d="M4 2.8 6.2 5 4 7.2" stroke="#fff" stroke-width="1.4" fill="none"/></svg>3 bedrooms and 2 ½ bathrooms</li>
        </ul>
      </div>
    </div>

    <div class="thumbs">
      <div class="photo photo--walkway" role="img" aria-label="Paved side walkway to the front door"></div>
      <div class="photo photo--interior" role="img" aria-label="Sunroom dining area with ceiling fan"></div>
      <div class="photo photo--kitchen" role="img" aria-label="Open kitchen and living room"></div>
    </div>

    <div class="feature">
      <div class="photo photo--exterior" role="img" aria-label="Street view of the home with garage and tropical trees"></div>
    </div>

    <footer class="footer">
      <div class="brand"><span class="brand-name">NORVALE<br>COMPANIES</span></div>
      <div class="contact">
        <p class="contact-lead">For Leasing Information, Kindly Contact</p>
        <p class="contact-name">DANA R. WHITFIELD</p>
      </div>
      <div class="reach">
        <p class="phone"><svg width="12" height="18" viewBox="0 0 12 18"><rect x="1" y="1" width="10" height="16" rx="2" fill="none" stroke="#1a6a9e" stroke-width="2"/></svg>561-555-0148</p>
        <p class="email"><svg width="12" height="9" viewBox="0 0 12 9"><rect width="12" height="9" fill="#1a6a9e"/><path d="M0 0 6 5 12 0" stroke="#fff" fill="none"/></svg>dana@norvalecompanies.com</p>
      </div>
    </footer>
  </section>

  <section class="page page--back">
    <header class="back-header">
      <h2 class="back-title">POOL HOME ON COVETED CORNER LOT<br>WITH OVERSIZED YARD.</h2>
    </header>

    <div class="back-hero">
      <div class="photo photo--dusk" role="img" aria-label="Corner lot home at dusk with landscaped front garden"></div>
    </div>

    <div class="back-thumbs">
      <div class="photo photo--pool" role="img" aria-label="Screened pool and patio"></div>
      <div class="photo photo--interior" role="img" aria-label="Bedroom with ceiling fan"></div>
      <div class="photo photo--yard" role="img" aria-label="Large backyard with patio seating"></div>
    </div>

    <div class="details">
      <div>
        <p>This impressive home boasts one of the largest yards in Palm Beach Gardens' most family friendly community, Linden Grove.</p>
        <p>Enjoy the ultimate Florida lifestyle with a beautiful pool &amp; expanded patio areas - perfect for entertaining.</p>
        <p>Upgraded features throughout.</p>
      </div>
      <ul>
        <li>Custom wood and ship lap details in all bathrooms and loft.</li>
        <li>New dark wood laminate flooring upstairs. New high-efficiency A/C units with smart thermostats.</li>
        <li>New pool pump and new heater controlled from your phone! Crown molding throughout.</li>
        <li>Walk-in closets. Quiet &amp; private cul-de-sac.</li>
      </ul>
    </div>

    <div class="back-lower">
      <div class="photo photo--kitchen" role="img" aria-label="White kitchen with dark counters"></div>
      <div class="photo photo--laundry" role="img" aria-label="Laundry room with washer and dryer"></div>
      <div class="photo photo--bath" role="img" aria-label="Bathroom with tiled walls"></div>
    </div>

    <footer class="footer">
      <div class="brand"><span class="brand-name">NORVALE<br>COMPANIES</span></div>
      <div class="contact">
        <p class="contact-lead">For Leasing Information, Kindly Contact</p>
        <p class="contact-name">DANA R. WHITFIELD</p>
      </div>
      <div class="reach">
        <p class="phone"><svg width="12" height="18" viewBox="0 0 12 18"><rect x="1" y="1" width="10" height="16" rx="2" fill="none" stroke="#1a6a9e" stroke-width="2"/></svg>561-555-0148</p>
        <p class="email"><svg width="12" height="9" viewBox="0 0 12 9"><rect width="12" height="9" fill="#1a6a9e"/><path d="M0 0 6 5 12 0" stroke="#fff" fill="none"/></svg>dana@norvalecompanies.com</p>
      </div>
    </footer>
  </section>

</main>
</body>
</html>
```